Etiketten-Design für Fruchtsäfte
Zielgruppe
Wir sind ein Obstbaubetrieb und suchen für unsere Fruchtsäfte ein neues modernes Etikett
Aufgabenstellung
Wir benötigen ein Etikett für unseren Pfirsichnektar, Kirschennektar, Marillennektar und Traubensaft.
Es kann sich hierbei um das selbe Muster handeln, nur bei der Bezeichnung sollte Wendlingers Marillennektar stehen.
Als Muster was wir uns vorstellen würden füge ich zwei Bilder von einem Obstbaukollegen hinzu.Wir sind aber für alles offen. Außerdem anbei unser Logo, wo nicht Obstbau Wendlinger stehen muss sondern vielleicht nur die Frucht in der Mitte und dann eben Wendlingers Traubensaft usw. Und auch anbei unsere aktuellen Etiketten. Vom Format her und Beschriftung sollte es ähnlich wie unsere alten Etiketten sein. Vielleicht nur etwas schmaler.

```html
<!DOCTYPE html>
<html lang="de">
<head>
<meta charset="utf-8">
<title>Wendlingers Fruchtsäfte – Etiketten</title>
<link rel="stylesheet" href="https://fonts.googleapis.com/css2?family=Fredoka:wght@400;500;600&family=Jost:wght@400;600&display=swap">
<style>
  :root {
    --page: #ffffff;
    --paper: #f5f2eb;
    --frame: #bdb9b0;
    --ink: #4a4a4a;
    --marille: #f0c234;
    --marille-fruit: #efc13e;
    --kirsche: #d6567e;
    --kirsche-fruit: #d2567a;
    --pfirsich: #e8cd2c;
    --pfirsich-fruit: #ecd53a;
    --traube: #3b3d8e;
    --traube-fruit: #45489a;
    --dot: #4fa37e;
  }
  * { box-sizing: border-box; margin: 0; padding: 0; }
  html, body { width: 1200px; height: 2400px; overflow: hidden; }
  body {
    background: var(--page);
    font-family: "Fredoka", "Jost", sans-serif;
    position: relative;
  }
  .label-sheet {
    position: absolute;
    inset: 0;
    display: grid;
    grid-template-columns: 310px 310px;
    grid-template-rows: 415px 415px;
    column-gap: 80px;
    row-gap: 735px;
    padding: 590px 0 0 252px;
  }
  .label {
    position: relative;
    width: 310px;
    height: 415px;
    background: var(--paper);
    box-shadow: 0 1px 6px rgba(0,0,0,0.08);
    overflow: hidden;
    color: var(--accent);
  }
  .label--marille { --accent: var(--marille); --fruit: var(--marille-fruit); }
  .label--kirsche { --accent: var(--kirsche); --fruit: var(--kirsche-fruit); }
  .label--pfirsich { --accent: var(--pfirsich); --fruit: var(--pfirsich-fruit); }
  .label--traube { --accent: var(--traube); --fruit: var(--traube-fruit); }

  .label__frame {
    position: absolute;
    inset: 8px;
    border: 1px solid var(--frame);
    pointer-events: none;
  }
  .label__brand {
    position: absolute;
    top: 26px;
    right: 42px;
    font-size: 26px;
    font-weight: 500;
    line-height: 1;
  }
  .label__product {
    position: absolute;
    top: 50px;
    left: 42px;
    font-size: 58px;
    font-weight: 600;
    line-height: 1;
    letter-spacing: -0.5px;
  }
  .label--traube .label__product { left: 66px; }
  .label__kind {
    position: absolute;
    top: 112px;
    right: 18px;
    font-size: 36px;
    font-weight: 600;
    line-height: 1;
  }
  .label__fruit-share {
    position: absolute;
    top: 170px;
    right: 28px;
    font-size: 11px;
    font-weight: 600;
    line-height: 1.2;
    letter-spacing: 0.3px;
  }
  .label__illustration {
    position: absolute;
    left: 45px;
    top: 160px;
    width: 150px;
    height: 172px;
    border-radius: 50%;
    background: radial-gradient(circle at 40% 35%, var(--fruit), var(--fruit) 60%, color-mix(in srgb, var(--fruit) 82%, #b0502a));
  }
  .label__illustration--edge {
    left: auto;
    right: -30px;
    top: 200px;
    width: 70px;
    height: 130px;
  }
  .label__footer {
    position: absolute;
    left: 18px;
    right: 16px;
    top: 325px;
    height: 75px;
    display: grid;
    grid-template-columns: 92px 1px 92px 1px 1fr;
    column-gap: 8px;
    align-items: start;
    font-family: "Jost", sans-serif;
    color: var(--ink);
  }
  .footer__divider {
    align-self: stretch;
    margin-top: 24px;
    margin-bottom: 6px;
    background: var(--ink);
    opacity: 0.6;
  }
  .producer__name {
    display: flex;
    align-items: center;
    gap: 4px;
    font-family: "Jost", sans-serif;
    font-size: 8px;
    font-weight: 600;
    color: var(--ink);
    line-height: 1;
    white-space: nowrap;
  }
  .producer__dot {
    width: 9px;
    height: 9px;
    border-radius: 50%;
    background: var(--dot);
    flex: none;
  }
  .producer__contact, .ingredients {
    font-size: 5px;
    line-height: 1.4;
    margin-top: 12px;
  }
  .ingredients { margin-top: 27px; }
  .ingredients strong { font-weight: 600; }
  .label__volume {
    margin-top: 30px;
    font-family: "Fredoka", sans-serif;
    font-size: 21px;
    font-weight: 500;
    line-height: 1;
    color: var(--accent);
    text-align: center;
  }
</style>
</head>
<body>
<main class="label-sheet">

  <article class="label label--marille">
    <div class="label__frame"></div>
    <div class="label__brand">Wendlingers</div>
    <h2 class="label__product">Marillen</h2>
    <div class="label__kind">Nektar</div>
    <div class="label__illustration" role="img" aria-label="Illustration einer Marille mit Blatt"></div>
    <div class="label__illustration label__illustration--edge" role="img" aria-label="Angeschnittene Marille am Etikettrand"></div>
    <p class="label__fruit-share">Fruchtanteil<br>mindesten 40%</p>
    <footer class="label__footer">
      <div class="producer">
        <div class="producer__name"><span class="producer__dot"></span>Obstbau Wendlinger</div>
        <p class="producer__contact">Lindenweg 12<br>AT-7100 Obersee<br>obstbau.wendlinger@postfach.at<br>www.obstbau-wendlinger.at<br>+43 660 4812937</p>
      </div>
      <span class="footer__divider"></span>
      <p class="ingredients">Durch Erhitzen haltbar gemacht<br><strong>Zutaten:</strong> Wasser, Marillenmark, Zucker<br><strong>Säuerungsmittel:</strong> Zitronensäure<br>Antioxidationsmittel: Ascorbinsäure<br><strong>mind. haltbar bis:</strong> siehe Verschluss</p>
      <span class="footer__divider"></span>
      <div class="label__volume">0,75l</div>
    </footer>
  </article>

  <article class="label label--kirsche">
    <div class="label__frame"></div>
    <div class="label__brand">Wendlingers</div>
    <h2 class="label__product">Kirschen</h2>
    <div class="label__kind">Nektar</div>
    <div class="label__illustration" role="img" aria-label="Illustration zweier Kirschen am Stiel mit Blatt"></div>
    <div class="label__illustration label__illustration--edge" role="img" aria-label="Angeschnittene Kirsche am Etikettrand"></div>
    <p class="label__fruit-share">Fruchtanteil<br>mindesten 40%</p>
    <footer class="label__footer">
      <div class="producer">
        <div class="producer__name"><span class="producer__dot"></span>Obstbau Wendlinger</div>
        <p class="producer__contact">Lindenweg 12<br>AT-7100 Obersee<br>obstbau.wendlinger@postfach.at<br>www.obstbau-wendlinger.at<br>+43 660 4812937</p>
      </div>
      <span class="footer__divider"></span>
      <p class="ingredients">Durch Erhitzen haltbar gemacht<br><strong>Zutaten:</strong> Wasser, Kirschenmark, Weichselmark, Zucker<br><strong>Säuerungsmittel:</strong> Zitronensäure<br>Antioxidationsmittel: Ascorbinsäure<br><strong>mind. haltbar bis:</strong> siehe Verschluss</p>
      <span class="footer__divider"></span>
      <div class="label__volume">0,75l</div>
    </footer>
  </article>

  <article class="label label--pfirsich">
    <div class="label__frame"></div>
    <div class="label__brand">Wendlingers</div>
    <h2 class="label__product">Pfirsich</h2>
    <div class="label__kind">Nektar</div>
    <div class="label__illustration" role="img" aria-label="Illustration eines Pfirsichs mit Blatt"></div>
    <div class="label__illustration label__illustration--edge" role="img" aria-label="Angeschnittener Pfirsich am Etikettrand"></div>
    <p class="label__fruit-share">Fruchtanteil<br>mindesten 40%</p>
    <footer class="label__footer">
      <div class="producer">
        <div class="producer__name"><span class="producer__dot"></span>Obstbau Wendlinger</div>
        <p class="producer__contact">Lindenweg 12<br>AT-7100 Obersee<br>obstbau.wendlinger@postfach.at<br>www.obstbau-wendlinger.at<br>+43 660 4812937</p>
      </div>
      <span class="footer__divider"></span>
      <p class="ingredients">Durch Erhitzen haltbar gemacht<br><strong>Zutaten:</strong> Wasser, Pfirsichmark, Zucker<br><strong>Säuerungsmittel:</strong> Zitronensäure<br>Antioxidationsmittel: Ascorbinsäure<br><strong>mind. haltbar bis:</strong> siehe Verschluss</p>
      <span class="footer__divider"></span>
      <div class="label__volume">0,75l</div>
    </footer>
  </article>

  <article class="label label--traube">
    <div class="label__frame"></div>
    <div class="label__brand">Wendlingers</div>
    <h2 class="label__product">Trauben</h2>
    <div class="label__kind">Saft</div>
    <div class="label__illustration" role="img" aria-label="Illustration einer Weintraube mit Blatt und Ranke"></div>
    <div class="label__illustration label__illustration--edge" role="img" aria-label="Angeschnittene Weintraube am Etikettrand"></div>
    <p class="label__fruit-share">Fruchtanteil<br>mindesten 40%</p>
    <footer class="label__footer">
      <div class="producer">
        <div class="producer__name"><span class="producer__dot"></span>Obstbau Wendlinger</div>
        <p class="producer__contact">Lindenweg 12<br>AT-7100 Obersee<br>obstbau.wendlinger@postfach.at<br>www.obstbau-wendlinger.at<br>+43 660 4812937</p>
      </div>
      <span class="footer__divider"></span>
      <p class="ingredients">Durch Erhitzen haltbar gemacht<br><strong>Zutaten:</strong> Traubensaft aus eigener Ernte<br><strong>Säuerungsmittel:</strong> Zitronensäure<br>Antioxidationsmittel: Ascorbinsäure<br><strong>mind. haltbar bis:</strong> siehe Verschluss</p>
      <span class="footer__divider"></span>
      <div class="label__volume">0,75l</div>
    </footer>
  </article>

</main>
</body>
</html>
```